Designing a "Fizzwhistle Parlour" Style Blog

I am clueless when it comes to technology and web design. I am starting a blog on pregnancy, babies and high society life in London. It's going to be called "Fizzwhistle Parlour", and will aim to be frank, funny and aspire to a certain type of luxury lifestyle.

I would like a well designed, sophisticated looking blog set up for me. I've never had a blog designed for me online before, so i am not entirely sure how it works but ideally i would like the whole "look set up" so i can get the password, add a domain to it and start inputting my text and pictures.

Basically i looked into setting up one myself on pagewright/postnook.com but i realised that with my very basic know how, what i was going to end up with from the "template suggestions" was going to be pretty generic and i really want something unique and special as i am going to try and promote this alongside my writing career.

I would like a relatively non-fussy layout but the "Fizzwhistle Parlour" title i thought could be designed to look like a bit of a logo, with perhaps a cocktail on one end and a dummy/rattle on the other. I want the whole website to look fashionable, stylish and endorse a "Fizzwhistle Parlour lifestyle".

Ideally it would be very easy for me to upload text and pictures to the blog and it would be very visually appealing to look at and easy to read. It will need to have a list of all my blog posts on the side (obviously which are yet to be written, but the capability to have them all in the readers eye-line when they are eventually written!)

I would like to blog to look more like a website than a standard blog. See www.thetweedwatcher.example or www.velvetquarterly.example for the type of non-standard blog format i like.

Each post is going to be mainly text but then i would like the ability to add photos to each one. I also want the text spread across the page so that it becomes "about the writing"... what i mean is some blogs have lots of little tabs of text you can click on... i want my blog to scroll down so you read it like a story... a bit like www.bumpdiaries.example or www.penandpearls.example.

Look forward to seeing what you come up with. as an example of my personal style, please see my website www.maisiebrook.example which was a clothing brand i designed a few years ago. See that i had an illustration of myself done (in the about section) i like the idea of some little drawings or something unique to make it original. Many thanks for your work in advance.

Please note, i have only made this work "refundable" because i havent done a web design style job post like this before and obviously have no idea whether this is something that would work (have someone design it online for me" BUT i fully intend to buy a design off here and am very serious about doing so so please know that if your design fits what i am looking for i am definitely buying it, this is a genuine committed request!

Many thanks

Reason: I am extending the deadline as i have just decided to Guarantee the prize money for the project. My email address is maisie@maisiebrook.example if you would like to email me any ideas/designs for the blog. Please know that i would like the actual blog set up for me on either pagewright or postnook.com site under FIZZWHISTLE PARLOUR (my new blog name). Obviously i will be buying the domain name for this but whoever comes up with the best design i will go onto whichever blog site you recommend, add register the FIZZWHISTLE PARLOUR BLOG and then you can do all the design for me. Then you will be guaranteed payment on this site. So just know - whoever describes and shows me through logos, fonts and description the best design for my blog will be the one to do it! And i definitely will be choosing someone! Hope my main description give you enough to work out what kind of a style i want. Very modern, femine, fresh fun and clear but not TACKY.. no gaudy colours or pictures.. i want it to look like a glossy magazine column. THANKS x

Target Market(s)

Target market are trendy london girls and new mothers and mothers-to-be. It should appeal to feminine stylish, educated women.

Industry/Entity Type

Clothing

Requirements
Must have
• It must be set up as a blog on an easy to naviagate blog site that i can have easy access to update with my text and pictures using a password and username. It should also be able to have a domain added to it so i can buy www.storiesofmayfairlane.example if i so wish in the future.

STORIES OF MAYFAIR LANE the title should be designed to look like a logo and be bold and stand out.

The Font needs to be clear yet stylish. I do not want it to be an "all uppercase" font. I am a writer, so i need the ability to use lowercase and uppercase lettering !

Please make it look very clean and clear cut so the reader knows exactly what shes looking at. Some blogs just look too messy, you dont know what you are meant to be reading.

I want the blog to make it clear what the latest blog post is and have that at the top then have all the other blog posts in an archive style list to the left or right of the page. Please make the font clear enough to read but not too huge.

I am sure this goes without saying, but Please note this blog MUST be completely suitable for the UK. I would like it on a UK blog site, or one that is completely worldwide and works for the UK. (ie if this blog is successful i want to make sure i can promote it/advertise on it with uk brands etc)

```html
<!DOCTYPE html>
<html lang="en">
<head>
<meta charset="utf-8">
<title>Fizzwhistle Parlour</title>
<link rel="stylesheet" href="https://fonts.googleapis.com/css2?family=Questrial&family=Arimo:ital,wght@0,400;0,700;1,400&display=swap">
<style>
:root{
  --bg-top:#3b474e;
  --bg-mid:#2a3338;
  --bg-deep:#1b1f22;
  --panel:#222324;
  --footer:#1f1f20;
  --widget:#262728;
  --widget-head:#2f3031;
  --rule:#3a3b3c;
  --title:#f2f2f2;
  --gold:#c9b98a;
  --meta:#a99b6d;
  --body:#9a9a9a;
  --white:#ffffff;
  --red:#c4141b;
  --red-dark:#7d0a0e;
  --page-box:#2c2d2e;
}
*{margin:0;padding:0;box-sizing:border-box}
html,body{width:869px;height:1200px;overflow:hidden}
body{
  position:relative;
  background:linear-gradient(180deg,var(--bg-top) 0,var(--bg-mid) 260px,#34404a 262px,#2b343b 700px,var(--bg-deep) 944px);
  font-family:"Arimo",Arial,sans-serif;
  color:var(--body);
}
.site-header{position:absolute;left:0;top:0;width:869px;height:58px}
.brand{position:absolute;left:21px;top:34px;font:700 16px "Arimo",Arial,sans-serif;color:var(--white)}
.main-nav{position:absolute;top:18px;left:0;font:400 13px "Questrial",sans-serif;color:#e6e9eb}
.main-nav a{position:absolute;white-space:nowrap;color:inherit;text-decoration:none}
.main-nav .raised{top:-8px}
.main-nav .raised::before{content:"";position:absolute;left:27px;top:-6px;border:3px solid transparent;border-top:4px solid #fff}

.content-panel{
  position:absolute;left:17px;top:58px;width:825px;height:884px;
  background:linear-gradient(180deg,#262728,var(--panel) 40%,#1d1e1f);
  border-radius:6px 6px 0 0;
  box-shadow:0 0 12px rgba(0,0,0,.6);
}
.content-panel::before{content:"";position:absolute;left:160px;top:-7px;border:7px solid transparent;border-top:0;border-bottom-color:#262728}

.post{position:absolute;left:58px;width:470px}
.post-title{font:400 23px "Questrial",sans-serif;color:var(--title);text-shadow:0 2px 3px #000;white-space:nowrap}
.post-title.large{font-size:31px}
.post-meta{position:absolute;left:0;font:italic 10px "Arimo",Arial,sans-serif;color:var(--meta);width:441px;padding-bottom:6px;border-bottom:1px solid var(--rule);white-space:nowrap}
.post-photo{position:absolute;left:2px;width:132px;height:133px;border:3px solid #e8e8e8;box-shadow:0 2px 6px #000}
.post-excerpt{position:absolute;left:153px;width:345px;font-size:10.4px;line-height:17.4px;color:var(--body);white-space:nowrap}
.read-more{position:absolute;left:361px;width:101px;height:26px;border-radius:13px;
  background:linear-gradient(180deg,#e0323a,var(--red) 55%,var(--red-dark));
  box-shadow:0 2px 4px #000;color:var(--white);font-size:11px;line-height:26px;padding-left:33px}
.read-more svg{position:absolute;left:9px;top:6px}

.pagination{position:absolute;left:58px;top:832px;display:flex;gap:8px}
.pagination span{width:31px;height:32px;background:var(--page-box);color:#ddd;font-size:11px;text-align:center;line-height:32px;box-shadow:0 1px 3px #000}
.pagination .current{background:var(--red)}

.widget{position:absolute;left:657px;width:197px;background:var(--widget);border-radius:4px;box-shadow:0 2px 8px #000}
.widget-title{height:39px;background:linear-gradient(180deg,#3a3b3c,var(--widget-head));font:400 16px "Questrial",sans-serif;color:var(--gold);padding:11px 0 0 22px;border-radius:4px 4px 0 0;position:relative}
.widget-title::before{content:"";position:absolute;left:0;top:12px;border:6px solid transparent;border-left-color:#4a4b4c}
.widget ul{list-style:none;padding:4px 0 6px}
.widget li,.footer-col li{position:relative;height:31.4px;line-height:31.4px;font-size:11px;color:var(--white);padding-left:45px;margin-right:10px;border-bottom:1px solid #303132;white-space:nowrap}
.widget li::before,.footer-col li::before{content:"";position:absolute;left:25px;top:12px;border:3.5px solid transparent;border-left:4px solid #cfcfcf}
.widget li.active{color:var(--gold);background:#1f2021}

.site-footer{position:absolute;left:0;top:944px;width:862px;height:256px;background:linear-gradient(180deg,#252526,var(--footer));box-shadow:0 -2px 6px #000}
.footer-col{position:absolute;top:34px;width:230px}
.footer-col h3{font:400 22px "Questrial",sans-serif;color:var(--gold);height:31px;border-bottom:1px solid var(--rule);padding-left:10px}
.footer-col ul{list-style:none}
.footer-col li{color:#aaa;padding-left:34px;margin:0}
.footer-col li::before{left:13px;border-left-color:#777}
</style>
</head>
<body>
<header class="site-header">
  <div class="brand">Fizzwhistle Parlour</div>
  <nav class="main-nav">
    <a style="left:156px">Home</a>
    <a style="left:208px">Get In Touch</a>
    <a style="left:296px">products</a>
    <a class="raised" style="left:361px">testimonials</a>
    <a style="left:439px">more stuff</a>
  </nav>
</header>

<main class="content-panel">
  <article class="post" style="top:48px">
    <h2 class="post-title">Fizzwhistle Parlour Psycho Gifs</h2>
    <p class="post-meta" style="top:40px">Posted by Admin on Feb 13 in Some Category, Another Categiry | 30 comments</p>
    <div class="post-photo" style="top:68px;background:linear-gradient(180deg,#b9a9a1,#6b5a5e 55%,#2a2830)" role="img" aria-label="Photo of a woman in a white blouse and black waistcoat holding a blue handbag"></div>
    <p class="post-excerpt" style="top:64px">Morbi condimentum tempus tincidunt. Sed neque ipsum, pulvinar eu<br>tristique sollicitudin, tincidunt at nisi. Aenean feugiat risus sed lacus<br>aliquam et adipiscing elit sodales. Aenean in erat sed neque convallis<br>convallis at eu metus. In varius lacus quis diam cursus posuere. Pellen-<br>tesque habitant morbi tristique senectus et netus et malesuada fames<br>ac turpis egestas. Class aptent taciti sociosqu ad litora torquent per<br>conubia nostra per inceptos...</p>
    <div class="read-more" style="top:189px"><svg width="14" height="14" viewBox="0 0 14 14"><circle cx="7" cy="7" r="6.5" fill="#eee"/><path d="M7 3.5V7l2.5 1.5" stroke="#888" stroke-width="1.2" fill="none"/></svg>Read More</div>
  </article>

  <article class="post" style="top:320px">
    <h2 class="post-title large">Daily Inspiration</h2>
    <p class="post-meta" style="top:44px">Posted by Admin on Feb 13 in Some Category, Another Categiry | 30 comments</p>
    <div class="post-photo" style="top:73px;background:linear-gradient(180deg,#8d8a84,#c8c2bc 40%,#3b52a8 65%,#5c5a55)" role="img" aria-label="Street photo of a woman in a white top, blue skirt and knitted hat"></div>
    <p class="post-excerpt" style="top:68px">Morbi condimentum tempus tincidunt. Sed neque ipsum, pulvinar eu<br>tristique sollicitudin, tincidunt at nisi. Aenean feugiat risus sed lacus<br>aliquam et adipiscing elit sodales. Aenean in erat sed neque convallis<br>convallis at eu metus. In varius lacus quis diam cursus posuere. Pellen-<br>tesque habitant morbi tristique senectus et netus et malesuada fames<br>ac turpis egestas. Class aptent taciti sociosqu ad litora torquent per<br>conubia nostra per inceptos...</p>
    <div class="read-more" style="top:190px"><svg width="14" height="14" viewBox="0 0 14 14"><circle cx="7" cy="7" r="6.5" fill="#eee"/><path d="M7 3.5V7l2.5 1.5" stroke="#888" stroke-width="1.2" fill="none"/></svg>Read More</div>
  </article>

  <article class="post" style="top:604px">
    <h2 class="post-title large">Thriftmark Gloves</h2>
    <p class="post-meta" style="top:44px">Posted by Admin on Feb 13 in Some Category, Another Categiry | 30 comments</p>
    <div class="post-photo" style="top:73px;background:linear-gradient(180deg,#f4f4f4,#2a2a2a 30%,#1a1a1a 80%,#f0f0f0)" role="img" aria-label="Product photo of black trousers with a black handbag and gloves"></div>
    <p class="post-excerpt" style="top:68px">Morbi condimentum tempus tincidunt. Sed neque ipsum, pulvinar eu<br>tristique sollicitudin, tincidunt at nisi. Aenean feugiat risus sed lacus<br>aliquam et adipiscing elit sodales. Aenean in erat sed neque convallis<br>convallis at eu metus. In varius lacus quis diam cursus posuere. Pellen-<br>tesque habitant morbi tristique senectus et netus et malesuada fames<br>ac turpis egestas. Class aptent taciti sociosqu ad litora torquent per<br>conubia nostra per inceptos...</p>
    <div class="read-more" style="top:185px"><svg width="14" height="14" viewBox="0 0 14 14"><circle cx="7" cy="7" r="6.5" fill="#eee"/></svg>Read More</div>
  </article>

  <nav class="pagination"><span>1</span><span class="current">2</span><span>3</span><span>4</span></nav>
</main>

<aside>
  <section class="widget" style="top:87px">
    <h3 class="widget-title">Topics Of Discussion</h3>
    <ul><li>Daily Inspiration</li><li class="active">Entertainment</li><li>Food and Drink</li><li>Featured Logos</li><li>Travel</li><li>Uncategorized</li></ul>
  </section>
  <section class="widget" style="top:359px">
    <h3 class="widget-title">Recent Posts</h3>
    <ul><li>Fizzwhistle Parlour Gifs</li><li>Daily Inspiration</li><li>Paris Pics</li><li>A Day Greek Pics</li><li>Thriftmark Gloves</li><li>Internet</li></ul>
  </section>
  <section class="widget" style="top:632px">
    <h3 class="widget-title">recent Comments</h3>
    <ul><li>Ana on Fizzwhistle Parlour</li><li>Tess Marlow On Daily</li><li>Inspiration</li><li>Pindle.com</li><li>In The News</li><li>Internet</li></ul>
  </section>
</aside>

<footer class="site-footer">
  <section class="footer-col" style="left:39px">
    <h3>Topics of Discussion</h3>
    <ul><li>Daily Inspiration</li><li>Entertainment</li><li>Food and Drinks</li><li>Featured Logos</li><li>Travel</li><li>Uncategorized</li></ul>
  </section>
  <section class="footer-col" style="left:318px">
    <h3>Recent Posts</h3>
    <ul><li>Fizzwhistle Parlour Gifs</li><li>Daily Inspiration</li><li>Paris Pics</li><li>A Day Greek Pics</li><li>Thriftmark Gloves</li><li>Internet</li></ul>
  </section>
  <section class="footer-col" style="left:606px">
    <h3>Recent Comments</h3>
    <ul><li>Ana on Fizzwhistle Parlour</li><li>Tess Marlow on Daily</li><li>Inspiration</li><li>Pindle.com</li><li>In The News</li><li>Internet</li></ul>
  </section>
</footer>
</body>
</html>
```